Property Management business needs Business cards designed

We provide a premium property management service based in Sydney's Norther Beaches. We want people to feel confident in choosing us to manage their investment properties. We offer a much more personalized service than other estate agents.
We want a modern clean design. Something that shows confidence without being complicated.
Logo attached.

Target Market(s)

35-70yo Male and Female with strong property portfolios within Sydney's Norther Beaches

Industry/Entity Type

Property Management

Contact Information for Business Card

Address: Suite 7, 12-14 Kelvin Parade, Harlow NSW 2188
Two separate named cards.
Tom Ardley - 0491 570 118 tom@harbourvaleestates.com.au
Clara Dunmore - 0491 570 263 clara@harbourvaleestates.com.au

Requirements
Must have
• Business logo, name, number, address, email.

```html
<!DOCTYPE html>
<html lang="en">
<head>
<meta charset="utf-8">
<title>Harbourvale Estates – Business Card</title>
<link rel="stylesheet" href="https://fonts.googleapis.com/css2?family=Roboto:wght@400;500;700&display=swap">
<style>
  :root {
    --page-bg: #d9dcdf;
    --teal: #0f7c82;
    --teal-deep: #0a5d66;
    --teal-light: #1a8f93;
    --cream: #e7e3cc;
    --card-white: #ffffff;
    --text-teal: #16787f;
    --logo-ink: #eeeadb;
  }
  * { box-sizing: border-box; margin: 0; padding: 0; }
  html, body {
    width: 1200px;
    height: 1200px;
    overflow: hidden;
    background: var(--page-bg);
    font-family: "Roboto", Arial, sans-serif;
  }
  .business-card {
    position: absolute;
    left: 100px;
    top: 294px;
    width: 1000px;
    height: 612px;
    background: var(--card-white);
    overflow: hidden;
    box-shadow: 0 10px 30px rgba(0,0,0,0.18);
  }
  .card-art {
    position: absolute;
    inset: 0;
    width: 100%;
    height: 100%;
  }
  .brand-name {
    position: absolute;
    right: 90px;
    top: 118px;
    color: var(--logo-ink);
    font-weight: 500;
    font-size: 46px;
    letter-spacing: 1px;
    text-transform: uppercase;
    white-space: nowrap;
  }
  .contact-block {
    position: absolute;
    left: 70px;
    top: 318px;
    color: var(--text-teal);
  }
  .person-name {
    font-weight: 700;
    font-size: 38px;
    margin-bottom: 18px;
  }
  .contact-line {
    display: flex;
    align-items: flex-start;
    gap: 16px;
    font-size: 27px;
    line-height: 34px;
    margin-bottom: 12px;
  }
  .contact-icon {
    flex: 0 0 26px;
    width: 26px;
    height: 34px;
    fill: var(--text-teal);
  }
</style>
</head>
<body>
  <section class="business-card">
    <svg class="card-art" viewBox="0 0 1000 612" preserveAspectRatio="none">
      <defs>
        <linearGradient id="tealField" x1="0" y1="0" x2="1" y2="1">
          <stop offset="0" stop-color="var(--teal-light)"/>
          <stop offset="0.55" stop-color="var(--teal)"/>
          <stop offset="1" stop-color="var(--teal-deep)"/>
        </linearGradient>
      </defs>
      <polygon class="header-field" role="img" aria-label="Teal faceted geometric backdrop"
               points="0,0 1000,0 1000,300 0,170" fill="url(#tealField)"/>
      <polygon class="accent-stripe" points="0,170 1000,300 1000,316 0,186" fill="var(--cream)"/>
    </svg>

    <div class="brand-name">Harbourvale Estates</div>

    <div class="contact-block">
      <h1 class="person-name">Tom Ardley</h1>
      <p class="contact-line">
        <svg class="contact-icon" viewBox="0 0 26 34" aria-hidden="true">
          <path d="M7 4h12a2 2 0 0 1 2 2v22a2 2 0 0 1-2 2H7a2 2 0 0 1-2-2V6a2 2 0 0 1 2-2zm1 4v12h10V8zm2 15v2h2v-2zm4 0v2h2v-2z"/>
        </svg>
        <span>0491 570 118</span>
      </p>
      <p class="contact-line">
        <svg class="contact-icon" viewBox="0 0 26 34" aria-hidden="true">
          <path d="M1 10h24v16H1zM2 11l11 8 11-8v2l-11 8-11-8z"/>
        </svg>
        <span>tom@harbourvaleestates.com.au</span>
      </p>
      <p class="contact-line">
        <svg class="contact-icon" viewBox="0 0 26 34" aria-hidden="true">
          <path d="M1 10h24L13 28z"/>
        </svg>
        <span>Suite 7, 12-14 Kelvin Parade,<br>Harlow NSW 2188</span>
      </p>
    </div>
  </section>
</body>
</html>
```